Tallowmere Capital Partners- Business Card

We need a professional business card that conveys confidence and trust. Strength. A modern and still yet, traditional financial planner/advisor format. I will upload a logo file or two, you do not have to use it, if it does not work for the design.

Target Market(s)

high net worth

Industry/Entity Type

Finance

Contact Information for Business Card

Address: 24836 Orchard Ave. Suite 400, Huntington Beach, CA 93518, website: tallowmerecap.example, ph # (555) 271-6094, email address: rpoulsen@tallowmerecap.example

```html
<!DOCTYPE html>
<html lang="en">
<head>
<meta charset="utf-8">
<title>Tallowmere Capital Partners – Business Card</title>
<link href="https://fonts.googleapis.com/css2?family=Arimo:wght@400;700&display=swap" rel="stylesheet">
<style>
  :root {
    --gold: #b8974a;
    --ink: #5a5a5a;
    --rule: #6d6d6d;
    --paper: #ffffff;
    --night: #1f1f24;
    --night-mark: #2b2b31;
    --backdrop: #e9e9ea;
  }
  * { box-sizing: border-box; margin: 0; padding: 0; }
  html, body { width: 1200px; height: 900px; overflow: hidden; }
  body {
    background: var(--backdrop);
    font-family: "Arimo", Arial, sans-serif;
    position: relative;
  }
  .card {
    position: absolute;
    width: 640px;
    height: 366px;
    border-radius: 18px;
    overflow: hidden;
  }
  .card-back {
    left: 460px;
    top: 50px;
    background: var(--night);
    display: flex;
    align-items: center;
    justify-content: center;
  }
  .back-wordmark {
    display: flex;
    align-items: center;
    gap: 14px;
    color: var(--night-mark);
    font-weight: 700;
    font-size: 26px;
    letter-spacing: 2px;
  }
  .back-wordmark .mark-square {
    width: 30px; height: 30px;
    border: 3px solid var(--night-mark);
  }
  .card-front {
    left: 100px;
    top: 450px;
    background: var(--paper);
  }
  .front-wave { position: absolute; left: 0; top: 0; width: 640px; height: 366px; }
  .brand {
    position: absolute;
    left: 40px;
    top: 70px;
    width: 210px;
    display: flex;
    flex-direction: column;
    align-items: center;
    gap: 12px;
    color: var(--gold);
    font-weight: 700;
    text-align: center;
  }
  .brand .mark-square {
    width: 60px; height: 60px;
    border: 3px solid var(--gold);
  }
  .brand-name { font-size: 17px; line-height: 1.3; letter-spacing: 1.5px; }
  .divider {
    position: absolute;
    left: 282px;
    top: 56px;
    width: 1.5px;
    height: 188px;
    background: var(--rule);
  }
  .details {
    position: absolute;
    left: 306px;
    top: 56px;
    width: 320px;
    color: var(--ink);
  }
  .person-name {
    color: var(--gold);
    font-weight: 700;
    font-size: 24px;
    letter-spacing: 0.5px;
  }
  .person-title { font-size: 18px; margin-top: 2px; }
  .address { font-size: 17px; line-height: 1.25; margin-top: 16px; }
  .contact-list { list-style: none; margin-top: 16px; font-size: 17px; line-height: 1.35; }
  .contact-list li { display: flex; align-items: center; gap: 8px; white-space: nowrap; }
  .contact-list svg { width: 16px; height: 16px; flex: none; }
</style>
</head>
<body>
  <section class="card card-back" aria-label="Business card back">
    <div class="back-wordmark"><span class="mark-square"></span>TALLOWMERE CAPITAL PARTNERS</div>
  </section>

  <section class="card card-front" aria-label="Business card front">
    <svg class="front-wave" viewBox="0 0 640 366" aria-hidden="true">
      <path d="M0 200 C70 250 220 288 470 300 C260 300 90 282 0 236 Z" fill="var(--gold)"/>
      <path d="M0 256 C120 298 300 306 430 302 C530 298 595 306 640 318 L640 366 L0 366 Z" fill="var(--gold)"/>
    </svg>

    <div class="brand">
      <span class="mark-square"></span>
      <span class="brand-name">TALLOWMERE<br>CAPITAL PARTNERS</span>
    </div>

    <div class="divider"></div>

    <div class="details">
      <h1 class="person-name">ROWAN POULSEN</h1>
      <p class="person-title">Manager</p>
      <p class="address">24836 Orchard Ave. Suite 400<br>Huntington Beach, CA 93518</p>
      <ul class="contact-list">
        <li>
          <svg viewBox="0 0 24 24" fill="none" stroke="var(--gold)" stroke-width="2"><path d="M5 3h4l2 5-3 2a12 12 0 0 0 6 6l2-3 5 2v4a2 2 0 0 1-2 2A17 17 0 0 1 3 5a2 2 0 0 1 2-2z"/></svg>
          (555) 271-6094
        </li>
        <li>
          <svg viewBox="0 0 24 24" fill="none" stroke="var(--gold)" stroke-width="2"><rect x="3" y="5" width="18" height="14" rx="2"/><path d="M3 7l9 6 9-6"/></svg>
          rpoulsen@tallowmerecap.example
        </li>
        <li>
          <svg viewBox="0 0 24 24" fill="none" stroke="var(--gold)" stroke-width="2"><circle cx="12" cy="12" r="9"/><path d="M3 12h18M12 3c3 3 3 15 0 18M12 3c-3 3-3 15 0 18"/></svg>
          tallowmerecap.example
        </li>
      </ul>
    </div>
  </section>
</body>
</html>
```